Investment Funding, Building and Construction

I need a design logo for my new business based out of Houston, TX called Kestrel Ridge Holdings LLC., We are a company looking to help fund and invest into other small/businesses that do not want to deal with the banking system. We also remodel, renovate, and build from the ground up anything from residential, industrial warehousing, and commercial buildings. We would like the design to express our great deal of passion that we have for the work, our dedication to helping the costumer/businesses receive their expectation of work and also our professionalism and commitment to making sure we get the job done as perfect as possible. We want to build your future!

Target Market(s)

Architects, Design Companies, Home Owners and Real Estate

Industry/Entity Type

Construction Company

Contact Information for Business Card

Name: Dorian Pellham
Position: CEO/President
Company Name: Kestrel Ridge Holdings LLC.,
Website: www.kestrelridgehold.example
Phone: 281-507-3619
Email: kestrelridgehold@mailbox.example, crewfundflow@mailbox.example

Font styles to use
Serif

Colors
f04a50
3377b5

Requirements
Must have
• Motivational, Inspiring, and Detailed oriented work but simple.
Nice to have
• I would like to see excitement and enthusiasm within the card.
Should not have
• The project can not be boring and lack of detail.

```html
<!DOCTYPE html>
<html lang="en">
<head>
<meta charset="utf-8">
<title>Kestrel Ridge Holdings LLC – Business Card</title>
<link rel="stylesheet" href="https://fonts.googleapis.com/css2?family=Source+Serif+4:wght@400;600;700&display=swap">
<style>
  :root {
    --card-blue: #2a77b7;
    --accent-red: #f04a50;
    --ink: #000000;
    --paper: #ffffff;
    --page: #ffffff;
  }
  html, body {
    margin: 0;
    padding: 0;
    width: 1148px;
    height: 1200px;
    overflow: hidden;
    background: var(--page);
  }
  .canvas {
    position: relative;
    width: 1148px;
    height: 1200px;
  }
  .business-card {
    position: absolute;
    left: 100px;
    top: 331px;
    width: 942px;
    height: 538px;
    background: var(--card-blue);
    font-family: "Source Serif 4", Georgia, serif;
    color: var(--paper);
  }
  .brand {
    position: absolute;
    left: 56px;
    top: 52px;
    display: flex;
    align-items: center;
    gap: 16px;
  }
  .company-name {
    margin: 0;
    font-size: 43px;
    font-weight: 700;
    line-height: 1;
  }
  .brand-mark {
    width: 16px;
    height: 16px;
    background: var(--accent-red);
    flex: none;
  }
  .holder {
    position: absolute;
    right: 39px;
    top: 256px;
    text-align: right;
  }
  .holder-name {
    margin: 0;
    font-size: 43px;
    font-weight: 700;
    line-height: 1.05;
  }
  .holder-title {
    margin: 0;
    font-size: 28px;
    font-weight: 600;
    line-height: 1.05;
  }
  .divider {
    position: absolute;
    left: 56px;
    top: 317px;
    width: 635px;
    height: 3px;
    background: var(--ink);
  }
  .contact-list {
    position: absolute;
    left: 50px;
    top: 334px;
    margin: 0;
    padding: 0;
    list-style: none;
    font-size: 29px;
    line-height: 37px;
  }
  .contact-item {
    position: relative;
    padding-left: 59px;
    height: 37px;
    white-space: nowrap;
  }
  .contact-icon {
    position: absolute;
    left: 0;
    top: 7px;
    width: 24px;
    height: 24px;
    fill: var(--ink);
  }
</style>
</head>
<body>
<div class="canvas">
  <section class="business-card" aria-label="Business card">
    <div class="brand">
      <h1 class="company-name">Kestrel Ridge Holdings LLC</h1>
      <span class="brand-mark" aria-hidden="true"></span>
    </div>

    <div class="holder">
      <p class="holder-name">Dorian Pellham</p>
      <p class="holder-title">CEO/President</p>
    </div>

    <div class="divider"></div>

    <ul class="contact-list">
      <li class="contact-item">
        <svg class="contact-icon" viewBox="0 0 24 24" aria-hidden="true">
          <path d="M6.6 10.8c1.4 2.8 3.8 5.1 6.6 6.6l2.2-2.2c.3-.3.7-.4 1-.2 1.1.4 2.3.6 3.6.6.6 0 1 .4 1 1V20c0 .6-.4 1-1 1C10.6 21 3 13.4 3 4c0-.6.4-1 1-1h3.5c.6 0 1 .4 1 1 0 1.3.2 2.5.6 3.6.1.3 0 .7-.2 1l-2.3 2.2z"/>
        </svg>
        281-507-3619
      </li>
      <li class="contact-item">
        <svg class="contact-icon" viewBox="0 0 24 24" aria-hidden="true">
          <path d="M2 6.5V5h20v1.5l-10 6.2z"/>
          <path d="M2 8.8l10 6.2 10-6.2V19H2z"/>
        </svg>
        kestrelridgehold@mailbox.example
      </li>
      <li class="contact-item">crewfundflow@mailbox.example</li>
      <li class="contact-item">
        <svg class="contact-icon" viewBox="0 0 24 24" aria-hidden="true">
          <path d="M12 2a10 10 0 1 0 0 20 10 10 0 0 0 0-20zm-1 17.9A8 8 0 0 1 4.2 10.2L9 15v1c0 1.1.9 2 2 2zm6.9-2.5c-.3-.8-1-1.4-1.9-1.4h-1v-3c0-.6-.4-1-1-1H8v-2h2c.6 0 1-.4 1-1V7h2c1.1 0 2-.9 2-2v-.4a8 8 0 0 1 2.9 12.8z"/>
        </svg>
        www.kestrelridgehold.example
      </li>
    </ul>
  </section>
</div>
</body>
</html>
```